PREMIUM AGENCY High End Business Card - A+++ Designers Wanted

** DO NOT ATTEMPT TO CONTACT ME THROUGH SEARCHING ON ZINTREL OR EMAILING ME THROUGH MY WEBSITE **

I need a fresh, contemporary business card designed using the logo attached (BRONSALK)

I have attached the font for BRONSALK

It must have a premium look and feel. The business card size must be STANDARD size.

You can submit either/both VERTICAL or HORIZONTAL designs.

FRONT: It must have the following sample information on

Paul Ardley
Director Operations
Mobile +61 452 118 906
Email paulardley@bronsalk.com
www.bronsalk.com

The REAR of the business card must have the words

CREATE INSPIRE TOMORROW

as part of the design, in the same font (NEXA) attached.

The words do not need to be in capitals, or on the same line, please design this as you see it best working.

ADDITIONAL INFORMATION
======================

The BRONSALK logo must be on the front of the card

I want Ultraviolet printing on the final design, to enhance either the NAME of the person OR the BRONSALK logo OR the words on the back of the card.

Target Market(s)

Agency, Advertising Agency, Creative, Designers

Industry/Entity Type

Media

Contact Information for Business Card

Design Agency, Contemporary, Premium look and feel, High Quality

Font styles to use
Serif
Sans Serif
Other font styles liked:
• ATTACHED TO PROJECT

Requirements
Must have
• BLACK & WHITE as the primary design, and if you feel there can be a highlighted colour, then this can be used.
• The Logo ICON attached is blue, this colour must not be changed.
• I have attached the partner brand BRONSALK MEDIA incase you need to manipulate the original files.
• ** DO NOT ATTEMPT TO CONTACT ME THROUGH SEARCHING ON ZINTREL OR EMAILING ME THROUGH MY WEBSITE **
Nice to have
• Must be Premium. I have attached some sample designs, that I like that would be a good inspiration for where this can be taken.
• My favourite design is is the KESTRAVUE2-BUSINESSCARD-TEMPLATE
Should not have
• No funny or silly standard / off the shelf designs

```html
<!DOCTYPE html>
<html lang="en">
<head>
<meta charset="utf-8">
<title>BRONSALK — Business Card, Front and Back</title>
<link href="https://fonts.googleapis.com/css2?family=Montserrat:wght@400;500;700;800&display=swap" rel="stylesheet">
<style>
  :root {
    --brand-blue: #0ea5ec;
    --brand-blue-deep: #0a86d6;
    --ink: #050505;
    --ink-soft: #1c1c1c;
    --paper: #ffffff;
    --stage: #e9ecee;
    --text-light: #f2f2f2;
  }
  * { box-sizing: border-box; margin: 0; padding: 0; }
  html, body {
    width: 1200px;
    height: 1000px;
    overflow: hidden;
    background: var(--stage);
    font-family: "Montserrat", sans-serif;
  }
  .stage {
    position: relative;
    width: 1200px;
    height: 1000px;
    display: flex;
    align-items: center;
    justify-content: center;
    gap: 100px;
  }
  .card {
    position: relative;
    width: 360px;
    height: 590px;
    overflow: hidden;
    background: radial-gradient(circle at 55% 45%, var(--ink-soft) 0%, var(--ink) 65%);
    box-shadow: 0 18px 40px rgba(0,0,0,0.18);
  }
  .card__shapes {
    position: absolute;
    inset: 0;
    width: 100%;
    height: 100%;
  }

  /* Wordmark */
  .wordmark {
    position: absolute;
    display: flex;
    align-items: center;
    gap: 12px;
    font-weight: 800;
    letter-spacing: 0.06em;
  }
  .wordmark__dot {
    width: 30px;
    height: 30px;
    border-radius: 50%;
    background: var(--brand-blue);
    flex: none;
  }

  /* Front */
  .card--front .wordmark {
    left: 44px;
    top: 118px;
    font-size: 38px;
    color: var(--ink);
  }
  .holder {
    position: absolute;
    left: 96px;
    top: 232px;
    color: var(--brand-blue);
  }
  .holder__first {
    font-size: 60px;
    font-weight: 700;
    line-height: 1;
  }
  .holder__last {
    font-size: 36px;
    font-weight: 700;
    line-height: 1.05;
  }
  .holder__role {
    margin-top: 6px;
    font-size: 16px;
    font-weight: 500;
    color: var(--text-light);
  }
  .contact {
    position: absolute;
    left: 96px;
    top: 402px;
    list-style: none;
    color: var(--text-light);
    font-size: 15px;
    font-weight: 500;
  }
  .contact li { height: 42px; line-height: 42px; }

  /* Back */
  .card--back .wordmark {
    left: 50%;
    top: 50%;
    transform: translate(-50%, -50%);
    font-size: 38px;
    color: var(--paper);
  }
  .tagline {
    position: absolute;
    left: 22px;
    bottom: 14px;
    font-size: 12px;
    font-weight: 700;
    letter-spacing: 0.04em;
    color: var(--paper);
  }
</style>
</head>
<body>
<main class="stage">

  <section class="card card--front" aria-label="Business card front">
    <svg class="card__shapes" viewBox="0 0 360 590" aria-hidden="true">
      <!-- white logo panel with blue top-right tab -->
      <rect x="0" y="0" width="360" height="205" fill="var(--paper)"/>
      <path d="M170 0 H360 V70 H230 Q205 70 198 45 Q190 0 170 0 Z" fill="var(--brand-blue)"/>
      <!-- blue left edge and contact tab -->
      <rect x="0" y="205" width="8" height="385" fill="var(--brand-blue)"/>
      <path d="M0 205 H30 Q62 205 62 240 V470 Q62 505 30 505 H0 Z" fill="var(--brand-blue)"/>
      <rect x="352" y="205" width="8" height="385" fill="var(--brand-blue)" opacity="0.9"/>
      <!-- phone icon -->
      <g transform="translate(22 413)" fill="var(--paper)">
        <path d="M3 1 L7 0 L9 5 L6.5 7 Q8 11 12 13 L14 10.5 L19 12.5 L18 16.5 Q10 18 4.5 12 Q0 6.5 3 1 Z"/>
      </g>
      <!-- send / email icon -->
      <g transform="translate(22 455)" fill="var(--paper)">
        <path d="M0 8 L19 0 L12 19 L9 11 Z"/>
      </g>
      <!-- globe / web icon -->
      <g transform="translate(31 507)" fill="none" stroke="var(--brand-blue)" stroke-width="1.6">
        <circle r="11" fill="var(--paper)" stroke="none"/>
        <ellipse rx="4.5" ry="10"/>
        <line x1="-10" y1="0" x2="10" y2="0"/>
        <line x1="-9" y1="-5" x2="9" y2="-5"/>
        <line x1="-9" y1="5" x2="9" y2="5"/>
      </g>
    </svg>

    <div class="wordmark"><span class="wordmark__dot"></span>BRONSALK</div>

    <div class="holder">
      <p class="holder__first">Paul</p>
      <p class="holder__last">Ardley</p>
      <p class="holder__role">Director Operations</p>
    </div>

    <ul class="contact">
      <li>+61 452 118 906</li>
      <li>paulardley@bronsalk.com</li>
      <li>www.bronsalk.com</li>
    </ul>
  </section>

  <section class="card card--back" aria-label="Business card back">
    <svg class="card__shapes" viewBox="0 0 360 590" aria-hidden="true">
      <rect x="0" y="0" width="8" height="590" fill="var(--brand-blue)"/>
      <rect x="0" y="582" width="360" height="8" fill="var(--brand-blue)"/>
      <path d="M0 548 H200 Q222 548 228 566 Q234 582 252 582 H0 Z" fill="var(--brand-blue)"/>
    </svg>

    <div class="wordmark"><span class="wordmark__dot"></span>BRONSALK</div>

    <p class="tagline">CREATE INSPIRE TOMORROW</p>
  </section>

</main>
</body>
</html>
```